Design new business card

I have an existing business card, but I would like a new design, more professional card

Target Market(s)

People that eat snacks, Men, Sports minded people, meat eaters,

Contact Information for Business Card

order@koruvanmeatcrisps.com
808-462-7390,
"Not All Beef Jerky Chips Are Created Equal"
"Thinnest, Crispiest, Best Tasting Beef Jerky Chip You'll Ever Try!"

Requirements
Must have
• Fundraising, Co-Packing Programs, Wholesale, Facebook & Instagram Icons
Free Shipping Available
www.koruvanmeatcrisps.com
Premium Beef Jerky Chips
Made in Hawaii Logo
MADE WITH 100% BORN & RAISED HAWAIIAN GRASS FED BEEF!!!
"NEVER EVER ANTIBIOTICS! NEVER EVER GROWTH HORMONES"
Should not have
• Photo of logo for creative ideas, do not cut and paste

```html
<!DOCTYPE html>
<html lang="en">
<head>
<meta charset="utf-8">
<title>Koruvan Meat Crisps – Business Card</title>
<link rel="stylesheet" href="https://fonts.googleapis.com/css2?family=Bangers&family=Cinzel:wght@700;900&family=Roboto:wght@400;500;700&display=swap">
<style>
  :root {
    --red: #c8070f;
    --gold: #e9ac2e;
    --black: #1c1c1c;
    --white: #f7f7f5;
    --ink: #1a1a1a;
    --grey-text: #333;
    --page: #d9d9d6;
    --mascot-brown: #8a5a37;
    --mascot-red: #b8141a;
  }
  * { box-sizing: border-box; margin: 0; padding: 0; }
  html, body { width: 1200px; height: 874px; overflow: hidden; }
  body {
    background: var(--page);
    font-family: "Roboto", Arial, sans-serif;
    position: relative;
  }
  .card {
    position: absolute;
    left: 240px;
    width: 720px;
    height: 400px;
    border-radius: 22px;
    overflow: hidden;
    box-shadow: 0 6px 18px rgba(0,0,0,.25);
  }
  /* ---------- Front ---------- */
  .card--front { top: 22px; background: var(--red); }
  .services {
    position: absolute; left: 60px; top: 38px;
    list-style: none; color: var(--white);
    font-size: 17px; line-height: 24px;
  }
  .services li { display: flex; align-items: center; gap: 10px; }
  .services svg { width: 15px; height: 15px; }
  .mascot {
    position: absolute; left: 440px; top: 80px;
    width: 230px; height: 320px;
    border-radius: 16px 16px 0 0;
    background: linear-gradient(180deg, var(--mascot-brown) 0%, var(--mascot-brown) 45%, var(--mascot-red) 100%);
  }
  .social {
    position: absolute; right: 26px; top: 26px; display: flex; gap: 4px;
  }
  .social span { width: 22px; height: 22px; border-radius: 4px; background: var(--white); }
  .headline {
    position: absolute; left: 38px; top: 190px;
    font-family: "Cinzel", Georgia, serif; font-weight: 900;
    line-height: 1;
  }
  .headline .premium { color: var(--white); font-size: 36px; display: block; }
  .headline .product { color: var(--gold); font-size: 32px; display: block; margin-top: 4px; }
  .band-shipping {
    position: absolute; left: 0; top: 282px; width: 440px; height: 50px;
    background: var(--black);
    display: flex; align-items: center; padding-left: 40px;
  }
  .band-shipping span {
    font-family: "Bangers", Impact, sans-serif; color: var(--gold);
    font-size: 30px; letter-spacing: 1.5px; font-style: italic;
  }
  .band-web {
    position: absolute; left: 400px; right: 0; top: 332px; height: 42px;
    background: var(--gold);
    display: flex; align-items: center; justify-content: center;
    font-weight: 700; font-size: 17px; color: var(--ink); white-space: nowrap;
  }
  /* ---------- Back ---------- */
  .card--back { top: 452px; background: var(--white); }
  .brand {
    position: absolute; left: 36px; top: 110px;
    display: flex; align-items: center; gap: 12px; width: 210px;
  }
  .brand-dot { width: 58px; height: 58px; flex: none; border-radius: 50%; background: var(--red); }
  .brand-name {
    font-family: "Cinzel", Georgia, serif; font-weight: 700;
    font-size: 19px; line-height: 1.2; color: var(--ink);
  }
  .divider {
    position: absolute; left: 262px; top: 70px; width: 1.5px; height: 190px;
    background: #555;
  }
  .person { position: absolute; left: 296px; top: 96px; }
  .person-name {
    font-family: "Cinzel", Georgia, serif; font-weight: 700;
    font-size: 30px; color: var(--ink); letter-spacing: .5px;
  }
  .person-title { color: var(--red); font-size: 17px; font-weight: 500; margin-top: -2px; }
  .contacts { list-style: none; margin-top: 16px; font-size: 18px; color: var(--grey-text); line-height: 26px; }
  .contacts li { display: flex; align-items: center; gap: 10px; }
  .contacts svg { width: 14px; height: 14px; fill: var(--ink); }
  .band-tagline {
    position: absolute; left: 0; right: 0; bottom: 0; height: 100px;
    background: var(--black);
  }
  .tagline {
    position: absolute; left: 40px; top: 24px;
    color: var(--gold); font-size: 19px; line-height: 26px; text-align: center; width: 560px;
  }
  .stripes { position: absolute; right: 0; bottom: 0; width: 150px; height: 100px; }
</style>
</head>
<body>

<section class="card card--front" aria-label="Card front">
  <ul class="services">
    <li><svg viewBox="0 0 16 16"><circle cx="8" cy="8" r="8" fill="#e9ac2e"/><path d="M4.5 8.3l2.3 2.3 4.7-4.8" stroke="#c8070f" stroke-width="2" fill="none"/></svg>Fundraising</li>
    <li><svg viewBox="0 0 16 16"><circle cx="8" cy="8" r="8" fill="#e9ac2e"/><path d="M4.5 8.3l2.3 2.3 4.7-4.8" stroke="#c8070f" stroke-width="2" fill="none"/></svg>Co-Packing Programs</li>
    <li><svg viewBox="0 0 16 16"><circle cx="8" cy="8" r="8" fill="#e9ac2e"/><path d="M4.5 8.3l2.3 2.3 4.7-4.8" stroke="#c8070f" stroke-width="2" fill="none"/></svg>Wholesale</li>
  </ul>

  <div class="mascot" role="img" aria-label="Illustration of a muscular bull mascot wearing red boxing gloves"></div>

  <div class="social" role="img" aria-label="Social media icons">
    <span></span><span></span>
  </div>

  <h1 class="headline">
    <span class="premium">PREMIUM</span>
    <span class="product">BEEF JERKY CHIPS</span>
  </h1>

  <div class="band-shipping"><span>FREE SHIPPING AVAILABLE</span></div>
  <div class="band-web">WWW.KORUVANMEATCRISPS.COM</div>
</section>

<section class="card card--back" aria-label="Card back">
  <div class="brand">
    <span class="brand-dot"></span>
    <span class="brand-name">Koruvan<br>Meat Crisps</span>
  </div>

  <div class="divider"></div>

  <div class="person">
    <h2 class="person-name">KAI MORRISON</h2>
    <p class="person-title">President</p>
    <ul class="contacts">
      <li><svg viewBox="0 0 24 24"><path d="M6.6 10.8a15.1 15.1 0 0 0 6.6 6.6l2.2-2.2c.3-.3.7-.4 1-.2 1.1.4 2.3.6 3.6.6.6 0 1 .4 1 1V20c0 .6-.4 1-1 1A17 17 0 0 1 3 4c0-.6.4-1 1-1h3.5c.6 0 1 .4 1 1 0 1.3.2 2.5.6 3.6.1.3 0 .7-.2 1z"/></svg>808-462-7390</li>
      <li><svg viewBox="0 0 24 24"><path d="M2 5h20v14H2z M2 5l10 8 10-8" stroke="#fff" stroke-width="1.5"/></svg>order@koruvanmeatcrisps.com</li>
      <li><svg viewBox="0 0 24 24"><circle cx="12" cy="12" r="10"/><path d="M2 12h20M12 2c3 3 3 17 0 20M12 2c-3 3-3 17 0 20" stroke="#fff" stroke-width="1.5" fill="none"/></svg>www.koruvanmeatcrisps.com</li>
    </ul>
  </div>

  <div class="band-tagline">
    <p class="tagline">Not All Beef Jerky Chips Are Created Equal<br>Thinnest, Crispiest, Best Tasting Beef Jerky Chip You'll Ever Try!</p>
    <svg class="stripes" viewBox="0 0 150 100" preserveAspectRatio="none" aria-hidden="true">
      <polygon points="40,100 70,0 100,0 70,100" fill="#e9ac2e"/>
      <polygon points="84,100 114,0 150,0 150,100" fill="#c8070f"/>
    </svg>
  </div>
</section>

</body>
</html>
```